psd/html for a e wallet payment website designed

hi
i am in need of a psd / html for a whole website designed
the site is a e wallet /payment system i can i will provide a link to what type of style i am looking for but i can not stress this enough i do not want anyone replicating the website i am just providing the links to show you what kind of function and the content that is involved also, i have a srs with detailed pages you can read and refer to if need be
thanks of viewing
Plimvora.com
Quindrel.com
brankowelt.com
Tazurnik.com

```html
<!DOCTYPE html>
<html lang="en">
<head>
<meta charset="utf-8">
<title>e-Wallet – secure payments</title>
<link href="https://fonts.googleapis.com/css2?family=Oswald:wght@300;400;500&family=Open+Sans:wght@400;600;700&family=Over+the+Rainbow&display=swap" rel="stylesheet">
<style>
:root{
  --cyan:#00a8c6;
  --cyan-dark:#0095b0;
  --charcoal:#2d2d2d;
  --charcoal-2:#333333;
  --sand:#f3e9df;
  --paper:#ffffff;
  --ink:#222222;
  --muted:#555555;
  --footer-grey:#e6e6e6;
  --logo-grey:#b5b5b5;
}
*{margin:0;padding:0;box-sizing:border-box}
html,body{width:982px;height:1200px;overflow:hidden;background:var(--paper)}
body{position:relative;font-family:"Open Sans",Arial,sans-serif;color:var(--ink)}
.abs{position:absolute}

/* top bar */
.topbar{left:0;top:0;width:982px;height:34px;background:var(--charcoal);color:#fff;font-size:12px}
.topbar .welcome{left:17px;top:9px;font-family:Arial,sans-serif}
.account-tab{left:722px;top:34px;width:226px;height:10px;background:var(--charcoal);clip-path:polygon(0 0,100% 0,96% 100%,4% 100%)}
.account-links{left:750px;top:10px;display:flex;gap:10px;align-items:center;font-family:Arial,sans-serif;font-size:11px}
.account-links svg{margin-right:12px}

/* header */
.header{left:0;top:34px;width:982px;height:158px;background:var(--cyan)}
.brand{left:20px;top:76px;font-family:"Open Sans",sans-serif;font-weight:700;font-size:42px;color:#fff;letter-spacing:-1px}
.nav{left:275px;top:117px;display:flex;height:55px}
.nav a{font-family:"Oswald",sans-serif;font-weight:300;font-size:26px;color:#fff;text-decoration:none;padding:14px 17px 0;text-transform:uppercase;letter-spacing:.2px}
.nav a.active{background:var(--charcoal)}
.nav-marker{left:305px;top:99px;width:0;height:0;border-left:12px solid transparent;border-right:12px solid transparent;border-top:13px solid var(--charcoal)}

/* hero */
.sand-band{left:0;top:492px;width:982px;height:253px;background:var(--sand)}
.hero{left:14px;top:172px;width:953px;height:342px;background:var(--charcoal);border:2px solid #3a3030}
.hero-photo{left:292px;top:2px;width:657px;height:336px;background:linear-gradient(110deg,#8a7466 0%,#c9b5a4 35%,#3a3a42 60%,#aab3bd 100%);clip-path:polygon(25% 0,100% 0,100% 100%,0 100%)}
.hero h1{left:27px;top:80px;font-family:"Oswald",sans-serif;font-weight:300;font-size:30px;color:#fff;letter-spacing:.3px}
.hero p{left:27px;top:126px;width:275px;font-family:Arial,sans-serif;font-size:12px;line-height:15px;color:#fff}
.cta{left:25px;top:229px;width:146px;height:40px;background:var(--cyan);border-radius:3px;font-family:"Oswald",sans-serif;font-weight:500;font-size:22px;color:var(--charcoal);text-align:center;line-height:40px;letter-spacing:-.3px}

/* features */
.feature{width:230px}
.feature h3{font-family:"Oswald",sans-serif;font-weight:500;font-size:19px;color:var(--cyan);letter-spacing:-.6px;line-height:22px}
.feature p{font-size:11.5px;line-height:14px;color:var(--ink);margin-top:2px}
.feature-icon{width:52px;height:52px}
.divider{height:6px;width:220px;background:radial-gradient(ellipse at center,rgba(150,120,90,.25),transparent 70%)}

/* welcome */
.welcome-title{left:17px;top:790px;font-size:31px;font-weight:400;color:var(--ink)}
.welcome-title b{font-weight:700}
.intro{left:20px;top:838px;width:530px;font-size:14px;line-height:18px;color:var(--muted)}
.intro a{color:var(--cyan);text-decoration:none}
.offer{width:260px}
.offer h4{font-size:18px;font-weight:600;color:var(--cyan)}
.offer p{font-size:11.5px;line-height:14.5px;color:var(--muted);margin-top:2px}
.offer .hand{font-family:"Over the Rainbow",cursive;font-size:14px;color:var(--ink);margin-top:3px}

.news{left:650px;top:796px;width:300px}
.news h2{font-size:25px;font-weight:600;color:var(--ink);letter-spacing:.3px}
.news ul{list-style:none;margin-top:16px}
.news li{position:relative;padding-left:22px;font-size:12px;line-height:14px;color:var(--cyan);margin-bottom:12px}
.news li::before{content:"";position:absolute;left:2px;top:4px;border-left:5px solid var(--cyan);border-top:3px solid transparent;border-bottom:3px solid transparent}

/* footer */
.footer-nav{left:0;top:1073px;width:982px;height:51px;background:var(--footer-grey)}
.footer-nav ul{position:absolute;left:15px;top:19px;display:flex;gap:17px;list-style:none;font-family:Arial,sans-serif;font-size:12px;color:var(--ink)}
.footer-brand{right:30px;top:10px;font-weight:700;font-size:24px;color:var(--logo-grey)}
.legal{left:13px;top:1144px;font-family:Arial,sans-serif;font-size:11px;line-height:18px;color:#000}
.badges{left:724px;top:1138px;display:flex;gap:14px;align-items:center}
.badge{height:34px;border-radius:3px;background:#e7e7e7}
</style>
</head>
<body>

<div class="abs topbar"><span class="abs welcome">Welcome to e-wallet</span></div>
<div class="abs account-tab"></div>
<div class="abs account-links" style="color:#fff">
  <svg width="32" height="22" viewBox="0 0 32 22" aria-hidden="true"><rect x="4" y="2" width="22" height="16" rx="2" fill="#eee"/><rect x="1" y="18" width="30" height="3" rx="1" fill="#eee"/><path d="M13 7l4 4" stroke="#555" stroke-width="1.5"/></svg>
  <span>sign up</span><span>sign in</span>
</div>

<header class="abs header"></header>
<div class="abs brand">e-Wallet</div>
<div class="abs nav-marker"></div>
<nav class="abs nav">
  <a class="active">Home</a><a>Personal</a><a>Business</a><a>Guide</a><a>Developers</a><a>Support</a>
</nav>

<div class="abs sand-band"></div>
<section class="abs hero">
  <div class="abs hero-photo" role="img" aria-label="Photo of a smiling couple using a laptop outdoors"></div>
  <h1 class="abs">ANYWHERE. ANYTIME.</h1>
  <p class="abs">Ut wisi enim ad minim veniam, quis nostrud exerci tation ullamcorper suscipit lobortis nisl ut aliquip ex ea commodo consequat. Duis autem vel eum iriure dolor in hendrerit in vulputate velit esse molestie consequat, vel illum dolore eu feugiat nulla facilisis at vero eros et accumsan et .</p>
  <div class="abs cta">SIGN UP NOW</div>
</section>

<!-- feature row 1 -->
<svg class="abs feature-icon" style="left:12px;top:545px" viewBox="0 0 52 52" aria-hidden="true"><path d="M30 4l-4 16" stroke="#2d2d2d" stroke-width="3"/><rect x="3" y="20" width="48" height="6" fill="#00a8c6"/><path d="M6 26h42l-4 22H10z" fill="#2d2d2d"/><g stroke="#fff" stroke-width="2.5"><path d="M16 31v12M22 31v12M28 31v12M34 31v12M40 31v12"/></g></svg>
<div class="abs feature" style="left:86px;top:548px"><h3>INSTANT TRANSACTIONS</h3><p>Payments to others are instant; there is no waiting for clearing of funds.</p></div>

<svg class="abs feature-icon" style="left:346px;top:545px" viewBox="0 0 52 52" aria-hidden="true"><rect x="3" y="12" width="48" height="34" rx="3" fill="#2d2d2d"/><rect x="3" y="18" width="48" height="6" fill="#00a8c6"/><rect x="10" y="30" width="14" height="4" fill="#fff"/></svg>
<div class="abs feature" style="left:417px;top:548px"><h3>MULTIPLE WALLETS</h3><p>Keep better track of your online funds with our wallet system.</p></div>

<svg class="abs feature-icon" style="left:675px;top:545px" viewBox="0 0 52 52" aria-hidden="true"><path d="M18 14V6h16v8" fill="none" stroke="#2d2d2d" stroke-width="3"/><rect x="2" y="14" width="48" height="34" rx="3" fill="#00a8c6"/><rect x="8" y="14" width="36" height="34" fill="#2d2d2d"/><path d="M20 26l6 6 6-6" stroke="#fff" stroke-width="2" fill="none"/></svg>
<div class="abs feature" style="left:745px;top:548px"><h3>EASY DEPOSIT &amp; WITHDRAW</h3><p>Simple transfers to and from your account, plus other flexible options.</p></div>

<div class="abs divider" style="left:50px;top:622px"></div>
<div class="abs divider" style="left:380px;top:622px"></div>
<div class="abs divider" style="left:710px;top:622px"></div>

<!-- feature row 2 -->
<svg class="abs feature-icon" style="left:15px;top:656px" viewBox="0 0 52 52" aria-hidden="true"><path d="M16 24V14a10 10 0 0 1 20 0v10" fill="none" stroke="#00a8c6" stroke-width="5"/><rect x="10" y="22" width="32" height="26" rx="3" fill="#2d2d2d"/><circle cx="26" cy="33" r="3.5" fill="#fff"/><rect x="24.5" y="34" width="3" height="7" fill="#fff"/></svg>
<div class="abs feature" style="left:86px;top:653px"><h3>SAFE AND SECURED</h3><p>The Plimvora website is built to protect your funds.</p></div>

<svg class="abs feature-icon" style="left:346px;top:656px" viewBox="0 0 52 52" aria-hidden="true"><ellipse cx="14" cy="30" rx="13" ry="9" fill="#2d2d2d"/><path d="M6 36l-4 8 10-5z" fill="#2d2d2d"/><ellipse cx="33" cy="16" rx="17" ry="12" fill="#00a8c6"/><path d="M38 26l6 9-12-7z" fill="#00a8c6"/></svg>
<div class="abs feature" style="left:417px;top:653px"><h3>24/7 CUSTOMER SUPPORT</h3><p>E-WALLET offers second to none customer support.</p></div>

<svg class="abs feature-icon" style="left:675px;top:656px" viewBox="0 0 52 52" aria-hidden="true"><path d="M3 4v44h47" fill="none" stroke="#2d2d2d" stroke-width="3"/><path d="M9 38l12-13 8 8 16-17" fill="none" stroke="#00a8c6" stroke-width="4"/><path d="M38 12h10v10z" fill="#00a8c6"/></svg>
<div class="abs feature" style="left:745px;top:653px"><h3>RESIDUAL AFFILIATE INCOME</h3><p>E-WALLET offers a simple yet extremely rewarding affiliate program.</p></div>

<!-- welcome -->
<h2 class="abs welcome-title">Welcome to <b>e-Wallet</b></h2>
<p class="abs intro">Tazurnik Transfer Technology is based on providing all its users with unique interfaces that allow to operate and control individual property rights for valuables (assets), stored at the specialized entities. <a>read more +</a></p>

<div class="abs offer" style="left:19px;top:912px"><h4>Shop Online</h4><p>Purchase products and services online with ease and confidence. Your personal information is never shared.</p><div class="hand">click here to sign up</div></div>
<div class="abs offer" style="left:319px;top:912px"><h4>Sell Online</h4><p>Accept payments from customers safely &amp; securely. Receive credit, debit card &amp; ewallet transfers instantly.</p><div class="hand">click here to sign up</div></div>

<aside class="abs news">
  <h2>LATEST NEWS</h2>
  <ul>
    <li>e-Wallet Wishes You a Happy New Year!</li>
    <li>e-Wallet users in Turkey can top-up their TZD purses via Verlo Telekom cash-in points</li>
    <li>You can buy Nova Credits of Miravo Online by paying with Tazurnik</li>
    <li>You can top-up your TZD purse by using Zentacash vouchers in Turkey</li>
    <li>Tazurnik Voice protects your phone conversations</li>
  </ul>
</aside>

<footer>
  <div class="abs footer-nav">
    <ul><li>Home</li><li>Personal Accounts</li><li>Business Accounts</li><li>Guide</li><li>Developers</li><li>Contact Us</li></ul>
    <div class="abs footer-brand">e-Wallet</div>
  </div>
  <div class="abs legal">Privacy Policy | FAQ | Terms of Use<br>COPYRIGHT © 2014. All Rights Reserved</div>
  <div class="abs badges">
    <div class="badge" style="width:56px"></div>
    <div class="badge" style="width:70px"></div>
    <div class="badge" style="width:86px"></div>
  </div>
</footer>

</body>
</html>
```